Kestrel Vitality a Centre Pty Ltd

Business card is to promote and represent our new business. It's situated in
47 Fenwick Road
Brookvale 2100 Sydney
Our clinic is all about getting people back to great health giving them back their lifestyle in half the usual time it takes to get results elsewhere , we do this through innovative therapies with latest state of the art equipment ,skills ,knowledge and experience.
We give them back their pain free healthy lifestyle with lots of energy to love life and perform their best Quickly and effectively .
The final design should communicate
Trust , confidence, results .
Updates

Reason: Waiting for some designers to submit work Thanks

Target Market(s)

High end clients that take their health and results seriously ,
High end athletes , as well as general people that want to see results with different
Treatment Methods and approach

Industry/Entity Type

Clinic

Contact Information for Business Card

Kestrel Vitality Centre Pty Ltd
47 Fenwick Road Brookvale 2100 Sydney
Website www.kestrelvitalitycentre.com.au

Font styles to use
Other font styles liked:
• Gothic font medium

Requirements
Must have
• A designe that makes people look twice with a wow factor , a designe that isn't like all the rest .
• Must have the logo in the colours Iv provided in my files
• Must communicate Trust, confidence , results
Nice to have
• 1) The logo raised up or
• 2) Maybe a pop up logo on the card ?
• Or let's be creative and have two cards one on top of the other so the two cards slide .... The front will have the kestrel logo with the address details etc
• The other card with have
• eg your next app .......................................repeating all way down the card
Should not have
• Basic plain looking card that everyone else has

```html
<!DOCTYPE html>
<html lang="en">
<head>
<meta charset="utf-8">
<title>Kestrel Vitality Centre – Business Card</title>
<link rel="stylesheet" href="https://fonts.googleapis.com/css2?family=Exo+2:wght@400;500;600&display=swap">
<style>
  :root {
    --backdrop: #5e5e60;
    --card-white: #ffffff;
    --card-shade: #eef0f3;
    --brand-navy: #34358f;
    --brand-blue: #2f6fc0;
    --band-light: #3aa3dc;
    --band-deep: #2a3f95;
    --ink: #2b2b33;
    --ink-soft: #4a4a57;
  }
  * { box-sizing: border-box; margin: 0; padding: 0; }
  html, body {
    width: 1200px; height: 750px; overflow: hidden;
    background: var(--backdrop);
    font-family: "Exo 2", "Segoe UI", sans-serif;
  }
  .canvas {
    width: 1200px; height: 750px;
    display: flex; align-items: center; justify-content: center; gap: 40px;
  }
  .card {
    position: relative;
    width: 540px; height: 309px;
    background: linear-gradient(160deg, var(--card-white) 55%, var(--card-shade));
    overflow: hidden;
    box-shadow: 0 6px 18px rgba(0,0,0,.35);
  }
  /* Front */
  .card--front { display: flex; align-items: center; justify-content: center; gap: 12px; }
  .brand-mark {
    width: 30px; height: 30px; border-radius: 50%;
    background: var(--brand-blue);
    flex: none;
  }
  .brand-name {
    font-weight: 600; font-size: 30px; color: var(--brand-navy);
    letter-spacing: .5px; line-height: 1;
  }
  /* Back */
  .accent-band {
    position: absolute; left: 340px; top: 92px; right: 0; bottom: 0;
    background: radial-gradient(ellipse at 35% 60%, var(--band-light), var(--band-deep) 85%);
  }
  .holder {
    position: absolute; top: 26px; right: 30px; text-align: right;
  }
  .holder__name {
    font-weight: 500; font-size: 15px; letter-spacing: 1.2px;
    color: var(--brand-navy); text-transform: uppercase;
  }
  .holder__role { font-size: 11px; color: var(--ink); margin-top: 2px; }
  .card--back .brand {
    position: absolute; left: 30px; top: 108px;
    display: flex; align-items: center; gap: 9px;
  }
  .card--back .brand-mark { width: 22px; height: 22px; }
  .card--back .brand-name { font-size: 21px; }
  .contact {
    position: absolute; left: 32px; top: 172px;
    list-style: none; font-size: 10.5px; color: var(--ink-soft);
  }
  .contact li { display: flex; align-items: center; gap: 7px; height: 17px; }
  .contact svg { width: 10px; height: 10px; fill: var(--brand-navy); flex: none; }
  .address {
    position: absolute; right: 30px; top: 150px; text-align: right;
    color: #fff; font-size: 13px; line-height: 1.45; letter-spacing: .4px;
  }
</style>
</head>
<body>
<main class="canvas">

  <section class="card card--front" aria-label="Card front">
    <span class="brand-mark"></span>
    <span class="brand-name">Kestrel Vitality Centre</span>
  </section>

  <section class="card card--back" aria-label="Card back">
    <div class="accent-band" role="img" aria-label="Blue flowing wave decoration"></div>

    <div class="holder">
      <p class="holder__name">Marcus Whitfield</p>
      <p class="holder__role">Managing Director</p>
    </div>

    <div class="brand">
      <span class="brand-mark"></span>
      <span class="brand-name">Kestrel Vitality Centre</span>
    </div>

    <ul class="contact">
      <li><svg viewBox="0 0 10 10"><path d="M2 0.5 3.6 2.6 2.7 3.8C3.3 5 4.9 6.7 6.2 7.3L7.4 6.4 9.5 8 8.3 9.5C4.6 9.2 0.8 5.4 0.5 1.7Z"/></svg>021 555 0147</li>
      <li><svg viewBox="0 0 10 10"><path d="M2.5 0h5v10h-5zM3.3 1v7h3.4V1z"/></svg>021 555 0148</li>
      <li><svg viewBox="0 0 10 10"><path d="M1 3h8v7H1zM3 0h4v3H3zM2.5 5h5v1h-5z"/></svg>021 555 0149</li>
      <li><svg viewBox="0 0 10 10"><path d="M0 2h10v6H0zM.8 2.6 5 5.6 9.2 2.6 5 4.6z" fill-rule="evenodd"/></svg>hello@kestrelmail.com</li>
      <li><svg viewBox="0 0 10 10"><path d="M5 0a5 5 0 1 0 0 10A5 5 0 0 0 5 0zm0 1.2a3.8 3.8 0 0 1 0 7.6 3.8 3.8 0 0 1 0-7.6zM1.5 4.5h7v1h-7zM4.5 1.2h1v7.6h-1z"/></svg>www.kestrelvitalitycentre.com.au</li>
    </ul>

    <p class="address">47 Fenwick Road<br>Brookvale 2100 Sydney</p>
  </section>

</main>
</body>
</html>
```